One-page magazine ad for accountant serving the non-profit industry

I am Certified Public Accountant placing a one-page ad in Lanternway Journal. The ad will be seen by churches and other non-profit organizations.
Lanternway Journal requires the following:
Accepted file formats:
a) Press ready PDF with all fonts embedded. OR
b) Flattened CMYK Abode Photoshop PSD or illustrator PDF or EPS with all fonts outlined.
Ad Specs:
Trim 8" x 10.5"
Live 7.5" x 10"
Bleed 8.25" x 10.75"

I would like the ad to state the following information:

Marcus T. Quillby, CPA, CGMA

I am Certified Public Accountant with over 30 years of experience serving the accounting and tax needs of churches and non-profit organizations.

Some of the services I can offer:

Audits, Reviews, Compilations
Bookkeeping Services
Payroll Taxes
501C3 - IRS exemption applications
Clergy Housing Allowance issues and Personal Taxes

```html
<!DOCTYPE html>
<html lang="en">
<head>
<meta charset="utf-8">
<title>Marcus T. Quillby, CPA, CGMA — Lanternway Journal Ad</title>
<link rel="stylesheet" href="https://fonts.googleapis.com/css2?family=Arimo:wght@400;700&family=Cabin:wght@400;500&display=swap">
<style>
  :root {
    --slate: #58636f;
    --olive-faint: rgba(160, 168, 96, 0.55);
    --ink: #111417;
    --rule: #202428;
    --paper: #ffffff;
    --text-light: #ffffff;
  }
  * { margin: 0; padding: 0; box-sizing: border-box; }
  html, body { width: 921px; height: 1200px; overflow: hidden; background: var(--paper); }
  .ad { position: relative; width: 921px; height: 1200px; background: var(--paper); }

  .ad-top { position: absolute; left: 0; top: 0; width: 921px; height: 889px; background: var(--slate); overflow: hidden; }
  .emblem-backdrop {
    position: absolute; left: 147px; top: 232px; width: 636px; height: 636px; border-radius: 50%;
    background: radial-gradient(circle, rgba(160,168,96,0.35) 0%, rgba(160,168,96,0.22) 45%, rgba(160,168,96,0) 72%);
  }

  .headline {
    position: absolute; left: 0; top: 56px; width: 100%; text-align: center;
    font-family: "Arimo", Arial, sans-serif; font-weight: 400; font-size: 57px; line-height: 78px;
    color: var(--text-light); letter-spacing: 1px;
  }
  .headline-rule { position: absolute; left: 119px; top: 226px; width: 695px; height: 4px; background: var(--rule); }

  .intro {
    position: absolute; left: 110px; top: 272px; width: 701px; text-align: center;
    font-family: "Cabin", "Gill Sans", sans-serif; font-size: 33px; line-height: 46px; color: var(--text-light);
  }

  .services-heading {
    position: absolute; left: 90px; top: 536px;
    font-family: "Arimo", Arial, sans-serif; font-size: 32px; color: var(--text-light);
  }
  .services {
    position: absolute; left: 91px; top: 598px; list-style: none;
    font-family: "Cabin", "Gill Sans", sans-serif; font-size: 30px; line-height: 44px; color: var(--text-light);
  }
  .services li::before { content: "•"; }

  .brand { position: absolute; left: 130px; top: 900px; width: 200px; text-align: center; }
  .brand-name {
    font-family: "Cabin", "Gill Sans", sans-serif; font-weight: 400; font-size: 46px; color: var(--ink);
    line-height: 120px;
  }
  .brand-rule { width: 131px; height: 3px; background: var(--ink); margin: 8px auto 18px; }
  .brand-tag {
    font-family: "Arimo", Arial, sans-serif; font-weight: 400; font-size: 26px; line-height: 36px; color: var(--ink);
  }

  .divider { position: absolute; left: 404px; top: 927px; width: 4px; height: 218px; background: var(--ink); }

  .contact {
    position: absolute; left: 430px; top: 966px; width: 460px; text-align: center;
    font-family: "Cabin", "Gill Sans", sans-serif; font-weight: 500; font-size: 26px; line-height: 37px; color: var(--ink);
  }
</style>
</head>
<body>
<main class="ad">
  <section class="ad-top">
    <div class="emblem-backdrop" role="img" aria-label="Faint laurel wreath surrounding a balance scale"></div>
    <h1 class="headline">MARCUS T. QUILLBY<br>CPA, CGMA</h1>
    <div class="headline-rule"></div>
    <p class="intro">I am a Certified Public Accountant with over 30 years of experience serving accounting and tax needs of churches and non-profit organizations.</p>
    <h2 class="services-heading">Some of the services I can offer:</h2>
    <ul class="services">
      <li>Audits, Reviews, Compilations</li>
      <li>Bookkeeping Services</li>
      <li>Payroll Taxes</li>
      <li>501C3 - IRS exemption applications</li>
      <li>Clergy Housing Allowance issues and Personal Taxes</li>
    </ul>
  </section>

  <div class="brand">
    <div class="brand-name">Quillby</div>
    <div class="brand-rule"></div>
    <div class="brand-tag">certified<br>public<br>accountant</div>
  </div>

  <div class="divider"></div>

  <address class="contact" style="font-style: normal;">
    Marcus T. Quillby, CPA, CGMA<br>
    email: marcus@quillbycpa.com<br>
    telephone: (555) 014-2290
  </address>
</main>
</body>
</html>
```